Travel video blogger needs website design

I need a website designed for my new travel video blog "Roaming Compass". I have only just started but need a website that is fairly simple and not too busy. I have a logo which I want on it (I have attached it to this project). I also want a link to all my other social medias on the main page (vidstreamhub, Snapmosaic and friendweave) and my videos as well. Here is a link to my vidstreamhub page for you to look at: https://www.vidstreamhub.example/channel/QXr7mPzT2wVn84KsdYe31jaB
As I have only just started and I am still trying to find my specific niche, again I need it to be sleek and simple that I can go in and change slightly here and there. I would like these pages on the website: About Me, Videos, Social Media, Blog, Gallery, contact me. for an example I like the look of www.wanderingkinfolk.example website.

I already have the domain and I am with Nestwarp with wordpress.org. I just want to spend my time getting better and learning about videos then trying to create a website (I am a bit of a perfectionist when I try to do something).

I

Target Market(s)

Young Adults (majority females) between the ages of 18 and 30 with an interest in travelling.

Industry/Entity Type

Travel Industry

Number of Pages Required

1 page

Colors

Designer to choose colors to be used in the design.

Requirements
Must have
• A like to my Snapmosaic, friendweave and vidstreamhub channels on the home page
• Must be a nice, simple design
• Must have my logo on the front and name "Roaming Compass"
Nice to have
• A nice light, bright coloured theme
Should not have
• A dark coloured theme

```html
<!DOCTYPE html>
<html lang="en">
<head>
<meta charset="utf-8">
<title>Roaming Compass</title>
<link href="https://fonts.googleapis.com/css2?family=Lora:wght@400;500&family=Arimo:wght@400;500&display=swap" rel="stylesheet">
<style>
:root{
  --page:#faf9f7;
  --white:#ffffff;
  --ink:#1c1c1c;
  --muted:#555555;
  --accent:#d9a86c;
  --sand:#f6e6d6;
  --line:#222222;
}
*{box-sizing:border-box;margin:0;padding:0}
html,body{width:1200px;height:2695px;overflow:hidden;background:var(--page)}
body{font-family:"Arimo",Arial,sans-serif;color:var(--ink)}
.page{position:relative;width:1200px;height:2695px;overflow:hidden;background:var(--page)}
.abs{position:absolute}

/* top bar */
.topbar{left:0;top:0;width:1200px;height:54px;background:var(--white)}
.top-social{left:226px;top:21px;width:160px;display:flex;gap:6px;font-size:8.5px;line-height:10px;color:var(--accent);white-space:nowrap;overflow:hidden}
.nav{left:394px;top:19px;display:flex;gap:24px;font-size:11.5px;letter-spacing:.4px;text-transform:uppercase;white-space:nowrap}
.nav a{color:var(--ink);text-decoration:none}
.nav a.active{color:var(--accent)}
.search{left:946px;top:15px;width:20px;height:20px;border-radius:50%;background:var(--accent)}
.brand-band{left:0;top:54px;width:1200px;height:96px;background:var(--white)}
.brand{left:0;top:76px;width:1200px;text-align:center}
.brand-dot{display:inline-block;width:46px;height:46px;border:2px solid var(--ink);border-radius:50%}
.brand-name{display:block;margin-top:6px;font-size:15px;font-weight:500;letter-spacing:1.5px;text-transform:uppercase;color:var(--ink)}

/* hero */
.hero{left:0;top:149px;width:1200px;height:336px;background:linear-gradient(100deg,#8aa3b3 0%,#c9d6dc 35%,#d8cfc2 60%,#b79578 78%,#2b2b2b 100%)}
.frame{border:2px solid var(--accent)}
.hero-frame{left:443px;top:255px;width:327px;height:146px}
.hero-card{left:431px;top:246px;width:327px;height:146px;background:var(--white);text-align:center;padding-top:22px}
.kicker{font-size:10px;letter-spacing:1px;text-transform:uppercase;color:var(--accent)}
.hero-title{font-family:"Lora",Georgia,serif;font-size:21px;line-height:1.4;margin-top:6px}
.link{font-family:"Lora",Georgia,serif;font-size:11.5px;text-decoration:underline;color:var(--ink)}
.hero-card .link{display:inline-block;margin-top:8px}

.tile{top:458px;width:226px;height:144px}
.tile-label{position:absolute;left:0;right:0;bottom:12px;text-align:center;font-family:"Lora",Georgia,serif;font-size:17px;color:var(--white)}
.tile-blog{left:234px;background:linear-gradient(135deg,#a8744f,#d9b77a 50%,#4d5a5f)}
.tile-about{left:483px;background:linear-gradient(135deg,#8d7a6a,#c7b39c 50%,#5c6a77)}
.tile-videos{left:733px;background:linear-gradient(135deg,#e9a357,#c86c3b 55%,#4e3a3a)}
.play{position:absolute;left:50%;top:44%;transform:translate(-50%,-50%)}

/* welcome */
.welcome{left:0;top:668px;width:600px;height:266px;background:var(--sand);text-align:center}
.welcome-mark{display:inline-block;margin-top:28px;width:38px;height:38px;border:2px solid var(--ink);border-radius:50%}
.welcome h2{font-family:"Lora",Georgia,serif;font-weight:400;font-size:22px;margin-top:14px}
.welcome p{width:300px;margin:10px auto 0;font-size:10px;line-height:1.6;color:var(--muted)}
.btn{display:inline-block;margin-top:16px;width:112px;height:33px;line-height:33px;background:var(--white);font-family:"Lora",Georgia,serif;font-size:11px;box-shadow:0 2px 6px rgba(0,0,0,.08)}
.welcome-photo{left:600px;top:668px;width:600px;height:266px;background:linear-gradient(120deg,#9fb08a,#e5d2bd 40%,#d9b19a 70%,#7c8a6a)}

/* stories */
.story-photo{width:296px;height:284px}
.story-frame{width:296px;height:282px}
.story-title{width:359px;height:99px;background:var(--white);padding:15px 18px}
.story-title h3{font-family:"Lora",Georgia,serif;font-weight:400;font-size:17.5px;line-height:1.45;margin-top:6px}
.story-text{width:385px;height:146px;background:var(--white);padding:20px 24px;font-size:10px;line-height:1.75;color:var(--muted)}
.story-text .link{display:inline-block;margin-top:6px}
.right{text-align:right}

/* feed */
.feed-icon{left:588px;top:2115px;width:22px;height:22px;border-radius:5px;background:var(--accent)}
.feed-head{left:0;top:2150px;width:1200px;text-align:center;font-family:"Lora",Georgia,serif;font-size:22px;font-weight:400}
.strip{top:2204px;width:200px;height:199px}

/* footer */
.footer-box{left:234px;top:2462px;width:732px;height:163px;border:2px solid var(--line);display:flex}
.fcol{flex:1;text-align:center;padding-top:22px}
.fcol+.fcol{border-left:2px solid var(--line)}
.fcol h4{font-family:"Lora",Georgia,serif;font-weight:400;font-size:14px}
.social-row{display:flex;justify-content:center;gap:6px;margin-top:14px;white-space:nowrap}
.social-row span{display:inline-flex;align-items:center;gap:4px;font-size:10px}
.social-row i{display:inline-block;width:12px;height:12px;border-radius:50%;background:var(--ink)}
.field{width:196px;height:31px;margin:12px auto 0;border:2px solid var(--line);line-height:27px;font-size:11px}
.sub{width:196px;height:31px;margin:8px auto 0;background:var(--white);line-height:31px;font-size:11px;box-shadow:0 2px 6px rgba(0,0,0,.08)}
.news{font-family:"Lora",Georgia,serif;font-size:11px;margin-top:12px}
.date{font-size:8px;color:var(--accent);margin-top:3px}
.copyright{left:0;top:2652px;width:1200px;text-align:center;font-size:10.5px}
</style>
</head>
<body>
<div class="page">

  <header class="abs topbar"></header>
  <div class="abs top-social"><span>Snapmosaic</span><span>friendweave</span><span>vidstreamhub</span></div>
  <nav class="abs nav">
    <a class="active" href="#">About Me</a><a href="#">Videos</a><a href="#">Social Media</a><a href="#">Blog</a><a href="#">Gallery</a><a href="#">Contact Me</a>
  </nav>
  <div class="abs search"></div>
  <div class="abs brand-band"></div>
  <div class="abs brand"><span class="brand-dot"></span><span class="brand-name">Roaming Compass</span></div>

  <div class="abs hero" role="img" aria-label="Photo of a woman holding a straw hat on a beach by the surf"></div>
  <div class="abs frame hero-frame"></div>
  <div class="abs hero-card">
    <div class="kicker">Good Feelings</div>
    <div class="hero-title">Good Feelings Come From<br>Good Heart</div>
    <a class="link" href="#">Read More</a>
  </div>

  <div class="abs tile tile-blog" role="img" aria-label="Photo of a straw hat, camera and drink on a table"><span class="tile-label">The Blog</span></div>
  <div class="abs tile tile-about" role="img" aria-label="Photo of a traveller looking at sea cliffs"><span class="tile-label">About Me</span></div>
  <div class="abs tile tile-videos" role="img" aria-label="Photo of friends celebrating at sunset">
    <svg class="play" width="30" height="30" viewBox="0 0 30 30"><path d="M9 5 L25 15 L9 25Z" fill="rgba(255,255,255,.85)"/></svg>
    <span class="tile-label">Videos</span>
  </div>

  <section class="abs welcome">
    <span class="welcome-mark"></span>
    <h2>Welcome to my Family!</h2>
    <p>Lorem ipsum dolor sit amet, consectetur adipiscing elit. Sed pharetra dignissim nunc vehicula tincidunt. Praesent nec nisl varius velit tempus sagittis at in tellus.</p>
    <span class="btn">Learn More</span>
  </section>
  <div class="abs welcome-photo" role="img" aria-label="Photo of friends toasting drinks outdoors"></div>

  <div class="abs frame story-frame" style="left:221px;top:1015px"></div>
  <div class="abs story-photo" style="left:234px;top:1000px;background:linear-gradient(160deg,#5d6b5a,#9aa08f 45%,#b9b2a5 75%,#7a7468)" role="img" aria-label="Photo of a hiker on a rocky mountain trail"></div>
  <div class="abs story-title" style="left:474px;top:1025px">
    <div class="kicker">Adventure</div>
    <h3>Lorem ipsum dolor sit amet, consectetur adipiscing elit.</h3>
  </div>
  <div class="abs story-text" style="left:580px;top:1149px">
    Etiam consectetur in metus in pellentesque. Proin at rhoncus dui. Donec dapibus est et libero ornare pulvinar. Cras eu molestie nunc, ut molestie sapien. Nunc vestibulum, nunc vitae elementum faucibus, ipsum neque efficitur metus, et mollis arcu nisl ut tortor. Etiam sed auctor ante.<br>
    <a class="link" href="#">Read More</a>
  </div>

  <div class="abs frame story-frame" style="left:682px;top:1368px;width:295px"></div>
  <div class="abs story-photo" style="left:670px;top:1354px;background:linear-gradient(160deg,#a9b1b0,#6f7776 50%,#c4b8a4)" role="img" aria-label="Photo of a traveller pulling a suitcase at a station">
    <svg class="play" width="34" height="34" viewBox="0 0 30 30"><path d="M9 5 L25 15 L9 25Z" fill="rgba(255,255,255,.85)"/></svg>
  </div>
  <div class="abs story-title right" style="left:366px;top:1379px">
    <div class="kicker">Travel</div>
    <h3>Lorem ipsum dolor sit amet, consectetur adipiscing elit.</h3>
  </div>
  <div class="abs story-text right" style="left:235px;top:1503px">
    Etiam consectetur in metus in pellentesque. Proin at rhoncus dui. Donec dapibus est et libero ornare pulvinar. Cras eu molestie nunc, ut molestie sapien. Nunc vestibulum, nunc vitae elementum faucibus, ipsum neque efficitur metus, et mollis arcu nisl ut tortor. Etiam sed auctor ante.<br>
    <a class="link" href="#">Read More</a>
  </div>

  <div class="abs frame story-frame" style="left:221px;top:1723px"></div>
  <div class="abs story-photo" style="left:234px;top:1708px;background:linear-gradient(180deg,#5fa6c4,#9cc7d6 45%,#c9c7be 70%,#6b6560)" role="img" aria-label="Photo of a woman raising her arms above a city"></div>
  <div class="abs story-title" style="left:474px;top:1733px">
    <div class="kicker">Life Style</div>
    <h3>Lorem ipsum dolor sit amet, consectetur adipiscing elit.</h3>
  </div>
  <div class="abs story-text" style="left:580px;top:1857px">
    Etiam consectetur in metus in pellentesque. Proin at rhoncus dui. Donec dapibus est et libero ornare pulvinar. Cras eu molestie nunc, ut molestie sapien. Nunc vestibulum, nunc vitae elementum faucibus, ipsum neque efficitur metus, et mollis arcu nisl ut tortor. Etiam sed auctor ante.<br>
    <a class="link" href="#">Read More</a>
  </div>

  <div class="abs feed-icon" aria-label="Snapmosaic"></div>
  <h2 class="abs feed-head">Let’s be my Snapmosaic Friends!</h2>
  <div class="abs strip" style="left:0;background:linear-gradient(135deg,#e9e6df,#e58a3c 60%,#4f7a3e)" role="img" aria-label="Photo of apricots and leaves on a table"></div>
  <div class="abs strip" style="left:200px;background:linear-gradient(135deg,#d9e6ea,#e3d2b4 55%,#8a7a63)" role="img" aria-label="Photo of a woman on a beach with her phone"></div>
  <div class="abs strip" style="left:400px;background:linear-gradient(135deg,#b38a4b,#7d8a5c 50%,#3f6b6a)" role="img" aria-label="Photo of a woman by a painted wooden door"></div>
  <div class="abs strip" style="left:600px;background:linear-gradient(135deg,#e7c6cc,#a8735a 55%,#f2eeee)" role="img" aria-label="Photo of a woman seen from behind with long hair"></div>
  <div class="abs strip" style="left:800px;background:linear-gradient(135deg,#b23a3a,#f1ede8 55%,#5a2a2a)" role="img" aria-label="Photo of an enamel camping mug"></div>
  <div class="abs strip" style="left:1000px;background:linear-gradient(180deg,#e9ecee,#b8bcbc 55%,#4e4a44)" role="img" aria-label="Photo of a woman with open arms on a cliff"></div>

  <footer class="abs footer-box">
    <div class="fcol">
      <h4>Follow me on social media</h4>
      <div class="social-row"><span><i></i>Snapmosaic</span><span><i></i>friendweave</span><span><i></i>vidstreamhub</span></div>
    </div>
    <div class="fcol">
      <h4>Subscribe Newsletter</h4>
      <div class="field">Enter Email Id</div>
      <div class="sub">Subscribe Now</div>
    </div>
    <div class="fcol">
      <h4>Latest News</h4>
      <div class="news">Lorem ipsum dolor sit amet, consect</div>
      <div class="date">11.03.2018</div>
      <div class="news">Etiam consectetur in metus in</div>
      <div class="date">11.03.2018</div>
    </div>
  </footer>
  <div class="abs copyright">© Copyright 2018 Roaming Compass</div>

</div>
</body>
</html>
```